Bluecrest Access & Mobility Elder Herald

We need an ad to run in various publications that highlights our products & services. Wheelchairs, Accessible Vans, Walkers, Scooters, Home Access & Auto access

```html
<!DOCTYPE html>
<html lang="en">
<head>
<meta charset="utf-8">
<title>Bluecrest Access &amp; Mobility – Rental Ad</title>
<link href="https://fonts.googleapis.com/css2?family=Oswald:wght@200;300;500;600&family=Poppins:wght@500;600;700&display=swap" rel="stylesheet">
<style>
  :root {
    --navy: #28255a;
    --mauve: #9a8c9c;
    --gold: #e0b978;
    --olive: #a0a576;
    --white: #ffffff;
    --van-blue: #5f7a9f;
  }
  html, body {
    margin: 0;
    padding: 0;
    width: 1200px;
    height: 1200px;
    overflow: hidden;
    background: var(--navy);
  }
  .ad {
    position: relative;
    width: 1200px;
    height: 1200px;
    overflow: hidden;
    background: var(--navy);
    font-family: "Poppins", sans-serif;
  }
  .ad-shapes {
    position: absolute;
    inset: 0;
  }
  .headline {
    position: absolute;
    left: 56px;
    top: 52px;
    margin: 0;
    font-family: "Oswald", sans-serif;
    font-weight: 600;
    font-size: 90px;
    line-height: 84px;
    color: var(--white);
    text-transform: uppercase;
    letter-spacing: -1px;
  }
  .headline .light { font-weight: 200; }

  .brand {
    position: absolute;
    left: 884px;
    top: 62px;
    width: 270px;
    display: flex;
    align-items: center;
    gap: 12px;
    color: var(--navy);
    font-family: "Poppins", sans-serif;
    font-weight: 600;
    font-size: 24px;
    line-height: 28px;
  }
  .brand-mark {
    flex: 0 0 auto;
    width: 42px;
    height: 42px;
    background: var(--navy);
  }

  .photo {
    position: absolute;
  }
  .photo-van {
    left: 372px;
    top: 252px;
    width: 768px;
    height: 368px;
    border-radius: 150px 200px 90px 60px;
    background: linear-gradient(135deg, #8aa0bf 0%, var(--van-blue) 55%, #3f5474 100%);
  }
  .product-circle {
    position: absolute;
    border-radius: 50%;
    display: flex;
    align-items: center;
    justify-content: center;
  }
  .product-circle .photo {
    position: static;
    border-radius: 50%;
  }
  .circle-powerchair { left: 139px; top: 369px; width: 208px; height: 208px; background: var(--white); }
  .circle-powerchair .photo { width: 130px; height: 130px; background: radial-gradient(circle, #6a6a70 0%, #c9c9cc 70%, #ffffff 100%); }
  .circle-walker { left: 614px; top: 666px; width: 176px; height: 176px; background: var(--white); }
  .circle-walker .photo { width: 96px; height: 96px; background: radial-gradient(circle, #7b7f99 0%, #d4d5de 70%, #ffffff 100%); }
  .circle-scooter { left: 959px; top: 666px; width: 176px; height: 176px; background: var(--gold); }
  .circle-scooter .photo { width: 120px; height: 120px; background: radial-gradient(circle, #8e2431 0%, #c46a5f 55%, var(--gold) 100%); }

  .pitch {
    position: absolute;
    left: 44px;
    top: 612px;
    width: 424px;
    margin: 0;
    text-align: center;
    font-family: "Oswald", sans-serif;
    font-weight: 300;
    font-size: 36px;
    line-height: 45px;
    color: var(--navy);
  }

  .call {
    position: absolute;
    left: 56px;
    top: 990px;
    color: var(--white);
  }
  .call-label {
    margin: 0;
    font-weight: 700;
    font-size: 21px;
    letter-spacing: 2px;
  }
  .call-tagline {
    margin: 0;
    font-weight: 600;
    font-size: 45px;
    line-height: 54px;
    letter-spacing: 3px;
  }
  .call-phone {
    margin: 0;
    font-weight: 700;
    font-size: 62px;
    line-height: 72px;
    letter-spacing: 6px;
    color: var(--gold);
  }

  .offer {
    position: absolute;
    left: 781px;
    top: 846px;
    color: var(--white);
    font-weight: 600;
  }
  .offer p { margin: 0; }
  .offer-get { font-size: 25px; line-height: 28px; }
  .offer-miles { font-size: 54px; line-height: 56px; }
  .offer-sub { font-size: 33px; line-height: 38px; }
  .offer-sub + .offer-sub { margin-top: 10px; }
  .offer-urge { font-size: 52px; line-height: 60px; margin-top: 14px !important; }
</style>
</head>
<body>
<main class="ad">
  <svg class="ad-shapes" width="1200" height="1200" viewBox="0 0 1200 1200" aria-hidden="true">
    <path class="panel-mauve" d="M0 0 H836 C850 250 700 560 420 660 C260 720 110 690 0 670 Z" fill="var(--mauve)"/>
    <path class="panel-white" d="M836 0 H1200 V180 C1080 230 920 225 860 150 C845 100 838 50 836 0 Z" fill="var(--white)"/>
    <g class="guide-lines" fill="none" stroke="var(--olive)" stroke-width="1.6">
      <path d="M0 888 C120 930 260 930 430 905 C560 880 680 810 870 620"/>
      <path d="M1007 215 C1000 280 990 320 975 340"/>
    </g>
    <circle class="disc-gold" cx="256" cy="730" r="243" fill="var(--gold)"/>
    <circle class="disc-olive" cx="951" cy="1052" r="296" fill="var(--olive)"/>
  </svg>

  <h1 class="headline">
    Access <span class="light">&amp;</span> Mobility<br>
    <span class="light">For</span> All Areas <span class="light">of</span><br>
    Your Life
  </h1>

  <div class="brand">
    <span class="brand-mark"></span>
    <span class="brand-name">Bluecrest Access &amp; Mobility</span>
  </div>

  <div class="photo photo-van" role="img" aria-label="Photo of a blue wheelchair accessible minivan with side ramp deployed, a couple with a wheelchair user at the door"></div>

  <div class="product-circle circle-powerchair">
    <div class="photo" role="img" aria-label="Photo of a power wheelchair"></div>
  </div>

  <p class="pitch">Don’t let your clients miss out on family vacations because of mobility issues.&nbsp; Rent a wheelchair accessible van for local or long distance travel.</p>

  <div class="product-circle circle-walker">
    <div class="photo" role="img" aria-label="Photo of a rolling walker"></div>
  </div>

  <div class="product-circle circle-scooter">
    <div class="photo" role="img" aria-label="Photo of a red mobility scooter"></div>
  </div>

  <div class="call">
    <p class="call-label">Call today:</p>
    <p class="call-tagline">Get Yours Reserved.</p>
    <p class="call-phone">970-555-0142</p>
  </div>

  <div class="offer">
    <p class="offer-get">GET</p>
    <p class="offer-miles">50 free miles</p>
    <p class="offer-sub">on your rental.</p>
    <p class="offer-sub">Rental reservations<br>are filling up,so</p>
    <p class="offer-urge">don’t delay!</p>
  </div>
</main>
</body>
</html>
```